Varnel Supply requires a new business card.

We are an online professional tool store.

Target Market(s)

We target the professional technician.

Industry/Entity Type

Business

Contact Information for Business Card

VarnelSupply.com.au

sales@varnelsupply.example

Requirements
Must have
• Needs to look commercial and professional
Should not have
• No Australian Colors, maps or shapes.
• No Shapes of Tools

```html
<!DOCTYPE html>
<html lang="en">
<head>
<meta charset="utf-8">
<title>Varnel Supply — Business Card</title>
<link rel="stylesheet" href="https://fonts.googleapis.com/css2?family=Quicksand:wght@500;700&display=swap">
<style>
  :root {
    --page-bg: #e9ecef;
    --card-white: #fbfbfc;
    --royal-blue: #3a55c4;
    --deep-blue: #2c3fa8;
    --teal: #17b4d4;
    --teal-dark: #0a8fb0;
    --teal-light: #22c4e0;
    --text-light: #ffffff;
    --shadow: 0 14px 30px rgba(20, 30, 60, 0.22);
  }
  * { box-sizing: border-box; margin: 0; padding: 0; }
  html, body {
    width: 1200px; height: 780px; overflow: hidden;
    background: var(--page-bg);
    font-family: "Quicksand", sans-serif;
  }
  .stage {
    width: 1200px; height: 780px;
    display: flex; align-items: center; justify-content: center; gap: 48px;
  }
  .card {
    position: relative;
    width: 520px; height: 300px;
    border-radius: 4px;
    overflow: hidden;
    box-shadow: var(--shadow);
  }

  /* Front */
  .card--front { background: var(--card-white); }
  .front-panels { position: absolute; inset: 0; }
  .holder {
    position: absolute; top: 26px; right: 30px; text-align: right;
  }
  .holder__name { color: var(--deep-blue); font-weight: 700; font-size: 22px; }
  .holder__role { color: var(--teal); font-weight: 500; font-size: 14px; margin-top: 2px; }
  .brand {
    position: absolute; top: 92px; right: 30px;
    display: flex; align-items: center; gap: 12px;
  }
  .brand__dot {
    width: 26px; height: 26px; border-radius: 50%; background: var(--teal);
  }
  .brand__name { color: var(--deep-blue); font-weight: 700; font-size: 30px; letter-spacing: 0.5px; }
  .contact {
    position: absolute; left: 30px; bottom: 60px;
    color: var(--text-light); font-weight: 500; font-size: 14px; line-height: 1.45;
  }
  .contact__line { display: flex; align-items: center; gap: 8px; }
  .contact__icon { width: 16px; height: 16px; flex: none; }
  .contact__address { margin-bottom: 4px; }
  .website-strip {
    position: absolute; left: 0; right: 0; bottom: 0; height: 40px;
    background: var(--teal);
    color: var(--text-light); font-weight: 500; font-size: 15px;
    display: flex; align-items: center; padding-left: 30px;
  }

  /* Back */
  .card--back {
    background: radial-gradient(ellipse at 55% 45%, var(--teal-light) 0%, var(--teal) 45%, var(--teal-dark) 100%);
    display: flex; flex-direction: column; align-items: center; justify-content: center;
    color: var(--text-light);
  }
  .back__name { font-weight: 700; font-size: 52px; letter-spacing: 1px; }
  .back__url { font-weight: 500; font-size: 14px; letter-spacing: 2px; margin-top: 18px; }
</style>
</head>
<body>
<main class="stage">
  <section class="card card--front" aria-label="Card front">
    <svg class="front-panels" width="520" height="300" viewBox="0 0 520 300" aria-hidden="true">
      <polygon points="0,170 280,150 520,150 520,300 0,300" fill="var(--royal-blue)"/>
      <polygon points="0,120 190,150 0,180" fill="var(--deep-blue)" opacity="0.35"/>
    </svg>

    <div class="holder">
      <p class="holder__name">Darren Holt</p>
      <p class="holder__role">Founder</p>
    </div>

    <div class="brand">
      <span class="brand__dot"></span>
      <span class="brand__name">Varnel Supply</span>
    </div>

    <div class="contact">
      <p class="contact__address">PO BOX 418 Keller Lane<br>Westbrook Industrial Park</p>
      <p class="contact__line">
        <svg class="contact__icon" viewBox="0 0 16 16" aria-hidden="true">
          <circle cx="8" cy="8" r="7.5" fill="none" stroke="#fff" stroke-width="1"/>
          <path d="M5.3 4.5l1.4 0 .6 1.8-.9.7a5 5 0 0 0 2.6 2.6l.7-.9 1.8.6v1.4c0 .4-.4.8-.8.8A6.4 6.4 0 0 1 4.5 5.3c0-.4.4-.8.8-.8z" fill="#fff"/>
        </svg>
        (555) 014-2286
      </p>
      <p class="contact__line">
        <svg class="contact__icon" viewBox="0 0 16 16" aria-hidden="true">
          <circle cx="8" cy="8" r="7.5" fill="none" stroke="#fff" stroke-width="1"/>
          <rect x="4" y="5.2" width="8" height="5.6" fill="#fff"/>
          <path d="M4 5.2l4 3 4-3" fill="none" stroke="var(--royal-blue)" stroke-width="0.9"/>
        </svg>
        sales@varnelsupply.example
      </p>
    </div>

    <div class="website-strip">VarnelSupply.com.au</div>
  </section>

  <section class="card card--back" aria-label="Card back">
    <p class="back__name">Varnel Supply</p>
    <p class="back__url">VarnelSupply.com.au</p>
  </section>
</main>
</body>
</html>
```